Studio Vela Hair Designers Business Card

I looking for a updated business card for a hair salon and me as a hairstylist. Something stylish and fun but not to whimsical. There has to be some seriousness about it to attract new clients. Basic imformation will be on the card. An abtract head will be okay but not neccessary. If it will fit, I would love to add my "Marlow Crown Wigs" logo and website (www.marlowcrownwigs.example). The "studio Vela Hair Designers logo is not an official logo, but my signage and some other things use that font. I'm open to an variation of the font and format or keep it as is.

Studio Vela
LORETTA QUINN
OWNER / STYLIST

HAIR RELAZING / STRAIGHTENING
EXTENSIONS / WEAVES
CUTS / CUSTOM COLOR
WIGS

20486 Tern Meadow Loop, Suite B
Irvine, CA 92614
(949) 555-0187
Email: studiovelahair@studiovelahair.example
www.studiovelahair.example
Updates

Please eliminate "Marlow Crown Wigs" logo...The focus of the b-card is "Studio Vela Hair Designers." The cards I have received so far has marlow crown wigs center stage. If there was room on the card in a side space, the logo would have been okay, but I don't have to have it on the card. Thanks                                   

Industry/Entity Type

Hair

```html
<!DOCTYPE html>
<html lang="en">
<head>
<meta charset="utf-8">
<title>Studio Vela Hair Designers – Business Card</title>
<link href="https://fonts.googleapis.com/css2?family=Cinzel:wght@400&family=Open+Sans:wght@400;600&display=swap" rel="stylesheet">
<style>
  :root {
    --page: #ffffff;
    --card-black: #000000;
    --wine: #3a0b08;
    --wine-deep: #1c0503;
    --accent-red: #e8252b;
    --ink-white: #ffffff;
  }
  * { margin: 0; padding: 0; box-sizing: border-box; }
  html, body {
    width: 1200px; height: 1000px; overflow: hidden;
    background: var(--page);
    font-family: "Open Sans", Arial, sans-serif;
  }
  .card {
    position: absolute;
    background: var(--card-black);
    overflow: hidden;
  }
  .card--front { left: 249px; top: 60px; width: 663px; height: 388px; }
  .card--back  { left: 249px; top: 538px; width: 666px; height: 390px; }
  .card__texture {
    position: absolute; inset: 0;
    background:
      radial-gradient(ellipse 55% 70% at 50% 45%, var(--wine) 0%, var(--wine-deep) 55%, var(--card-black) 100%);
  }
  .card__content { position: absolute; inset: 0; }

  /* Front */
  .brand-name {
    position: absolute; left: 0; right: 0; top: 196px;
    text-align: center;
    font-family: "Cinzel", Georgia, serif;
    font-size: 40px; letter-spacing: 1px;
    color: var(--ink-white);
  }
  .front-url {
    position: absolute; left: 0; right: 0; top: 292px;
    text-align: center;
    font-size: 23px; color: var(--ink-white);
    padding-left: 12px;
  }

  /* Back */
  .services { position: absolute; left: 30px; top: 55px; list-style: none; }
  .services__item {
    display: flex; align-items: center;
    height: 32.5px;
    font-size: 15px; color: var(--accent-red);
  }
  .services__icon { width: 32px; height: 30px; margin-right: 1px; }
  .owner { position: absolute; right: 60px; top: 58px; text-align: right; }
  .owner__name {
    font-family: "Cinzel", Georgia, serif;
    font-size: 27px; color: var(--ink-white); letter-spacing: 0.5px;
  }
  .owner__role { font-size: 19px; color: var(--ink-white); margin-top: 2px; }

  .contact { position: absolute; top: 278px; display: flex; align-items: flex-start; }
  .contact--address { left: 50px; }
  .contact--phone   { left: 246px; }
  .contact--email   { left: 375px; }
  .contact__icon {
    width: 28px; height: 29px; background: var(--accent-red);
    display: flex; align-items: center; justify-content: center;
    margin-right: 7px; flex: none;
  }
  .contact__text { font-size: 10px; line-height: 21px; color: var(--ink-white); margin-top: -6px; }
</style>
</head>
<body>

<section class="card card--front">
  <div class="card__texture" role="img" aria-label="Dark wine-red flourish damask pattern fading into black"></div>
  <div class="card__content">
    <div class="brand-name">Studio Vela Hair Designers</div>
    <div class="front-url">www.marlowcrownwigs.example</div>
  </div>
</section>

<section class="card card--back">
  <div class="card__texture" role="img" aria-label="Dark wine-red flourish damask pattern fading into black"></div>
  <div class="card__content">
    <ul class="services">
      <li class="services__item">
        <svg class="services__icon" viewBox="0 0 32 30"><g fill="none" stroke="#fff" stroke-width="1.2"><circle cx="6" cy="20" r="3"/><circle cx="10" cy="26" r="3"/></g><line x1="8" y1="18" x2="28" y2="4" stroke="#e8252b" stroke-width="1.5"/><line x1="11" y1="23" x2="30" y2="8" stroke="#fff" stroke-width="1.5"/></svg>
        Hair relazing / Straightwning
      </li>
      <li class="services__item">
        <svg class="services__icon" viewBox="0 0 32 30"><g fill="none" stroke="#fff" stroke-width="1.2"><circle cx="6" cy="20" r="3"/><circle cx="10" cy="26" r="3"/></g><line x1="8" y1="18" x2="28" y2="4" stroke="#e8252b" stroke-width="1.5"/><line x1="11" y1="23" x2="30" y2="8" stroke="#fff" stroke-width="1.5"/></svg>
        Extensions / Weaves
      </li>
      <li class="services__item">
        <svg class="services__icon" viewBox="0 0 32 30"><g fill="none" stroke="#fff" stroke-width="1.2"><circle cx="6" cy="20" r="3"/><circle cx="10" cy="26" r="3"/></g><line x1="8" y1="18" x2="28" y2="4" stroke="#e8252b" stroke-width="1.5"/><line x1="11" y1="23" x2="30" y2="8" stroke="#fff" stroke-width="1.5"/></svg>
        Cuts / Custom Color
      </li>
      <li class="services__item">
        <svg class="services__icon" viewBox="0 0 32 30"><g fill="none" stroke="#fff" stroke-width="1.2"><circle cx="6" cy="20" r="3"/><circle cx="10" cy="26" r="3"/></g><line x1="8" y1="18" x2="28" y2="4" stroke="#e8252b" stroke-width="1.5"/><line x1="11" y1="23" x2="30" y2="8" stroke="#fff" stroke-width="1.5"/></svg>
        Wigs
      </li>
    </ul>

    <div class="owner">
      <div class="owner__name">Loretta Quinn</div>
      <div class="owner__role">Owner / Stylist</div>
    </div>

    <div class="contact contact--address">
      <span class="contact__icon">
        <svg width="22" height="20" viewBox="0 0 22 20"><path d="M11 1 L1 10 L3 10 L11 3 L19 10 L21 10 Z" fill="#fff"/><path d="M4 11 L11 5 L18 11 V19 H13 V14 H9 V19 H4 Z" fill="#fff"/></svg>
      </span>
      <div class="contact__text">20486 Tern Meadow Loop, Suite B<br>Irvine, CA 92614</div>
    </div>

    <div class="contact contact--phone">
      <span class="contact__icon">
        <svg width="18" height="18" viewBox="0 0 24 24"><path fill="#fff" d="M6.6 10.8a15.1 15.1 0 0 0 6.6 6.6l2.2-2.2a1 1 0 0 1 1-.25 11.4 11.4 0 0 0 3.6.57 1 1 0 0 1 1 1V20a1 1 0 0 1-1 1A17 17 0 0 1 3 4a1 1 0 0 1 1-1h3.5a1 1 0 0 1 1 1c0 1.25.2 2.45.57 3.57a1 1 0 0 1-.25 1z"/></svg>
      </span>
      <div class="contact__text">(949) 555-0187</div>
    </div>

    <div class="contact contact--email">
      <span class="contact__icon">
        <svg width="18" height="18" viewBox="0 0 24 24"><circle cx="12" cy="12" r="4" fill="none" stroke="#fff" stroke-width="2.4"/><path d="M16 8v5.5a2.5 2.5 0 0 0 5 0V12a9 9 0 1 0-3.5 7.1" fill="none" stroke="#fff" stroke-width="2.4"/></svg>
      </span>
      <div class="contact__text">studiovelahair@studiovelahair.example</div>
    </div>
  </div>
</section>

</body>
</html>
```